Edgy rebranded biz cards KRB

We are rebranding our 20 yr old mortgage company with a new logo and would like cards to compliment our new look.

Target Market(s)

potential home buyers or clients for refinance

Industry/Entity Type

Mortgage Brokerage

Contact Information for Business Card

418 W. Lomita Ave #305
Henderson, NV 89152
702.519.4827 o
702-519-4829 f
www.kestrelridgelending,example
nmls 842019
KRB is an equal housing lender

Font styles to use
Sans Serif

Colors
0455a3
3176b5
0393ce
33a6d7

Requirements
Must have
• space for a photo
Nice to have
• One side with the company info and the other with the person's info

```html
<!DOCTYPE html>
<html lang="en">
<head>
<meta charset="utf-8">
<title>Kestrel Ridge Lending – Business Cards</title>
<link rel="stylesheet" href="https://fonts.googleapis.com/css2?family=Montserrat:ital,wght@0,400;0,700;1,400&display=swap">
<style>
  :root {
    --brand-deep: #0455a3;
    --brand-mid: #3176b5;
    --brand-bright: #0393ce;
    --brand-sky: #33a6d7;
    --ink-blue: #1f6fb5;
    --label-orange: #f0962a;
    --paper: #ffffff;
    --backdrop: #f4f4f4;
    --rule: #b9c9da;
  }
  * { margin: 0; padding: 0; box-sizing: border-box; }
  html, body { width: 1200px; height: 1200px; overflow: hidden; }
  body {
    background: var(--backdrop);
    font-family: "Montserrat", sans-serif;
    position: relative;
  }
  .card {
    position: absolute;
    width: 774px;
    height: 442px;
    background: var(--paper);
    overflow: hidden;
  }
  .card--company { left: 212px; top: 142px; }
  .card--person { left: 213px; top: 615px; }

  .wordmark {
    position: absolute;
    display: flex;
    align-items: center;
    gap: 12px;
    color: var(--brand-mid);
    font-weight: 700;
  }
  .wordmark__square {
    width: 34px; height: 34px;
    background: var(--brand-mid);
    flex: none;
  }
  .wordmark__text { display: flex; flex-direction: column; line-height: 1; }
  .wordmark__initials { font-size: 40px; letter-spacing: 1px; }
  .wordmark__name { font-size: 15px; letter-spacing: 0.5px; margin-top: 6px; text-transform: uppercase; }
  .card--company .wordmark { left: 55px; top: 84px; }
  .card--person .wordmark { left: 78px; top: 183px; }

  .contact {
    position: absolute;
    font-size: 21px;
    line-height: 26px;
    color: var(--ink-blue);
    font-weight: 400;
  }
  .contact__label { color: var(--label-orange); }
  .card--company .contact { left: 60px; top: 208px; }

  .panel-art { position: absolute; inset: 0; width: 774px; height: 442px; }
  .web-address {
    position: absolute;
    right: 28px; top: 390px;
    color: #ffffff;
    font-size: 18px;
    letter-spacing: 0.2px;
    white-space: nowrap;
  }

  .divider {
    position: absolute;
    left: 348px; top: 64px;
    width: 1px; height: 314px;
    background: var(--rule);
  }
  .person {
    position: absolute;
    left: 412px; top: 66px;
    color: var(--brand-deep);
  }
  .person__name { font-size: 32px; font-weight: 700; line-height: 40px; color: #0b63ad; }
  .person__title { font-size: 20px; font-style: italic; line-height: 24px; color: var(--ink-blue); }
  .card--person .contact { left: 414px; top: 177px; line-height: 25px; }
  .contact__group + .contact__group { margin-top: 6px; }
</style>
</head>
<body>

<section class="card card--company">
  <svg class="panel-art" viewBox="0 0 1246 712" preserveAspectRatio="none">
    <defs>
      <linearGradient id="grayBand" x1="0" y1="0" x2="0" y2="1">
        <stop offset="0" stop-color="#ffffff"/>
        <stop offset="1" stop-color="#c6c6ca"/>
      </linearGradient>
      <linearGradient id="photoTone" x1="0" y1="0" x2="0.4" y2="1">
        <stop offset="0" stop-color="#5c9fd6"/>
        <stop offset="0.45" stop-color="#2f6aa6"/>
        <stop offset="1" stop-color="#1d4a85"/>
      </linearGradient>
      <linearGradient id="blueBand" x1="0" y1="0" x2="0.4" y2="1">
        <stop offset="0" stop-color="#3176b5" stop-opacity="0"/>
        <stop offset="0.5" stop-color="#3176b5" stop-opacity="0.45"/>
        <stop offset="1" stop-color="#3176b5" stop-opacity="0.7"/>
      </linearGradient>
    </defs>
    <polygon points="835,0 1048,0 650,712 438,712" fill="url(#grayBand)"/>
    <g role="img" aria-label="Photo of a shingled two-storey house with gabled roof and pine trees against blue mountains">
      <polygon points="1048,0 1246,0 1246,712 650,712" fill="url(#photoTone)"/>
    </g>
    <polygon points="498,101 663,21 1048,712 833,712" fill="url(#blueBand)"/>
  </svg>

  <div class="wordmark">
    <span class="wordmark__square"></span>
    <span class="wordmark__text">
      <span class="wordmark__initials">KRB</span>
      <span class="wordmark__name">Kestrel Ridge Lending</span>
    </span>
  </div>

  <div class="contact">
    <p class="contact__label">Address :</p>
    <p>418 W. Lomita Ave #305</p>
    <p>Henderson, NV 89152</p>
    <p class="contact__label">Phone :</p>
    <p>(702) 519-4827</p>
    <p class="contact__label">Fax :</p>
    <p>(702) 519-4829</p>
  </div>

  <p class="web-address">www.kestrelridgelending.example</p>
</section>

<section class="card card--person">
  <div class="wordmark">
    <span class="wordmark__square"></span>
    <span class="wordmark__text">
      <span class="wordmark__initials">KRB</span>
      <span class="wordmark__name">Kestrel Ridge Lending</span>
    </span>
  </div>

  <div class="divider"></div>

  <div class="person">
    <h1 class="person__name">Marisol Avery</h1>
    <p class="person__title">Loan Officer</p>
  </div>

  <div class="contact">
    <div class="contact__group">
      <p class="contact__label">Address :</p>
      <p>Las Vegas, Nevada,</p>
      <p>United States</p>
    </div>
    <div class="contact__group">
      <p class="contact__label">Phone :</p>
      <p>(702) 555-0148</p>
      <p>(702) 555-0148</p>
    </div>
    <div class="contact__group">
      <p class="contact__label">Website:</p>
      <p>marisolhomeloans.example</p>
    </div>
  </div>
</section>

</body>
</html>
```